Flyer-Design für Audio und Video Installationen
Zielgruppe
Die Firma Kellerhof Audio und Video Installationen wurde im Jahr 1997 von Matthias Kellerhof gegründet und im Handelsregister eingetragen. In der Anfangszeit waren wir als Subunternehmer der Firma orvi-netlink tätig und haben massgeblich zur Sanierung der hausinternen Verkabelung im Raum Winterthur beigetragen.
Auch im Bereich des TV- und Radioempfangs via Parabolantenne sind wir Ihr Spezialist – vom Einfamilienhaus mit einem oder mehreren Empfangsgeräten, bis zu grossen Überbauungen oder Hotelanlagen mit Satellitenaufbereitungsanlagen.
In den ersten Stunden von Fiber to the home (FTTH) im Jahr 2010, wurden wir angefragt, die ersten Glasfaser-anschlüsse im Auftrag der Telvora zu realisieren. Seither arbeiten permanent 3 – 4 unserer Teams im Auftrag der Telvora und der Gemeindewerk Lindmatt für die Erstellung von FTTH Anschlüssen.
Ausserdem sind wir im Bereich Industrie, Banken und Versicherungen für verschiedene Partner im Einsatz um LWL-Installationen zu planen und zu erstellen, sowohl Multimode als auch Singlemode.
Kellerhof Audio und Video Installationen ist ein Kleinbetrieb mit momentan 10 Mitarbeitern aus den Bereichen Multimediaelektroniker und Elektromonteure.
Wir sind durch unsere Begeisterung für die neueste Technik, durch die tägliche Praxis und viele Weiter-bildungen trotz des schnellen Wandels der heutigen Technik stets auf dem neuesten Stand.
Aufgabenstellung
Das Hauptaugenmerk sollte auf Glasfaser, FTTH, LumaKet,c Installationen liegen. Eventuell möchte ich noch ein Angebot/Dienstleistung mit Preis Platzieren. OTO Dose (Glasfasersteckdose) vom Kommunikationsverteiler in ein anderes Zimmer verlegen, da in diesen Verteiler oft zuwenig Platz ist für Modem, Router etc.

```html
<!DOCTYPE html>
<html lang="de">
<head>
<meta charset="utf-8">
<title>Kellerhof Flyer – Titelseite und Rückseite</title>
<link rel="stylesheet" href="https://fonts.googleapis.com/css2?family=Roboto:wght@300;400;500;700;900&family=Roboto+Condensed:wght@700&family=Ubuntu:wght@400&display=swap">
<style>
  :root {
    --green: #5a9a2f;
    --red: #c0141f;
    --band: #c9c9c9;
    --ink: #1c1c1c;
    --mark: #d4d4d4;
    --paper: #ffffff;
    --bg: #ffffff;
  }
  * { margin: 0; padding: 0; box-sizing: border-box; }
  html, body { width: 1200px; height: 1200px; overflow: hidden; background: var(--bg); }
  body { position: relative; font-family: "Roboto", sans-serif; color: var(--ink); }

  .page-label {
    position: absolute; top: 146px; width: 406px; text-align: center;
    font-family: "Ubuntu", sans-serif; font-size: 24px; color: #111;
  }
  .page-label--front { left: 162px; }
  .page-label--back { left: 635px; }

  .panel {
    position: absolute; top: 207px; width: 406px; height: 853px;
    background: var(--paper); overflow: hidden;
    box-shadow: 0 2px 6px rgba(0,0,0,.35);
  }
  .panel--front { left: 162px; }
  .panel--back { left: 635px; }
  .band { position: absolute; left: 0; width: 100%; background: var(--band); }
  .band--top { top: 0; height: 20px; }
  .band--bottom { bottom: 0; height: 21px; }

  /* Front */
  .photo { position: absolute; }
  .photo--main { left: 0; top: 23px; width: 406px; height: 280px;
    background: linear-gradient(135deg, #4a4f57 0%, #8a8e92 45%, #d2d5d8 75%, #b9a98f 100%); }
  .photo--sat { left: 0; top: 306px; width: 133px; height: 93px;
    background: linear-gradient(160deg, #7f8890 0%, #5d5348 60%, #2f2a24 100%); }
  .photo--connectors { left: 136px; top: 306px; width: 133px; height: 93px;
    background: linear-gradient(160deg, #c9d0d6 0%, #56707f 60%, #2c3a44 100%); }
  .photo--cables { left: 272px; top: 306px; width: 134px; height: 93px;
    background: linear-gradient(160deg, #2e3c7a 0%, #6a6f80 50%, #d8c25a 75%, #b53a30 100%); }

  .services-line { position: absolute; left: 0; top: 407px; width: 100%; text-align: center;
    font-size: 18.5px; font-weight: 400; letter-spacing: -0.2px; }

  .badge { position: absolute; border-radius: 50%; background: var(--red); color: #fff;
    border: 2px solid #fff; box-shadow: 0 1px 4px rgba(0,0,0,.35);
    display: flex; align-items: center; justify-content: center; text-align: center;
    font-weight: 700; line-height: 1.05; }
  .badge--partner { left: 253px; top: 449px; width: 100px; height: 100px; font-size: 15.5px;
    transform: rotate(-10deg); }
  .badge--solution { left: 288px; top: 152px; width: 100px; height: 100px; font-size: 15.5px;
    transform: rotate(8deg); }

  /* Brand: plain square beside the company name */
  .brand { position: absolute; display: flex; align-items: center; }
  .brand-square { background: var(--mark); flex: none; }
  .brand-name { font-weight: 700; color: var(--ink); white-space: nowrap; }
  .brand--front { left: 0; top: 590px; width: 100%; justify-content: center; gap: 14px; }
  .brand--front .brand-square { width: 34px; height: 34px; }
  .brand--front .brand-name { font-size: 27px; letter-spacing: 7px; }
  .brand--back { left: 17px; top: 776px; gap: 7px; }
  .brand--back .brand-square { width: 14px; height: 14px; }
  .brand--back .brand-name { font-size: 11px; letter-spacing: 2.5px; }

  .web { position: absolute; color: var(--green); font-weight: 500; font-size: 19px; }
  .web--front { left: 0; top: 800px; width: 100%; text-align: center; }
  .web--back { left: 155px; top: 800px; }

  /* Back */
  .headline { position: absolute; left: 17px; top: 26px; width: 380px;
    color: var(--green); font-weight: 500; font-size: 22.5px; line-height: 26px; }
  .diagram { position: absolute; left: 16px; top: 84px; width: 360px; height: 290px;
    background: linear-gradient(180deg, #ffffff 0%, #f1f1f1 55%, #e7ebe4 100%); }
  .diagram-partner { position: absolute; left: 222px; top: 100px; font-size: 10.5px;
    font-weight: 500; color: #555; }

  .offer-band { position: absolute; left: 0; top: 396px; width: 100%; height: 72px; background: var(--band); }
  .offer-text { position: absolute; left: 17px; top: 404px; width: 210px;
    font-size: 15px; font-weight: 500; line-height: 18.5px; color: #111; }
  .price-box { position: absolute; left: 228px; top: 378px; width: 162px; height: 82px;
    background: #fff; box-shadow: 0 1px 4px rgba(0,0,0,.3); text-align: center; color: var(--red); }
  .price-label { margin-top: 6px; font-size: 11px; font-weight: 700; }
  .price-value { font-family: "Roboto Condensed", sans-serif; font-weight: 700; font-size: 54px; line-height: 54px; }

  .intro { position: absolute; left: 17px; top: 484px; width: 373px;
    font-size: 15.3px; font-weight: 300; line-height: 18.6px; text-align: justify; color: #111; }
  .services { position: absolute; left: 17px; top: 570px; width: 380px; list-style: none; }
  .services li { position: relative; padding-left: 20px; font-size: 15.3px; font-weight: 300;
    line-height: 20px; margin-bottom: 4.5px; color: #111; }
  .services li::before { content: ""; position: absolute; left: 0; top: 4px;
    border-left: 15px solid var(--green); border-top: 6px solid transparent; border-bottom: 6px solid transparent; }

  .contact { position: absolute; left: 155px; top: 748px; font-size: 11px; line-height: 14.3px;
    color: #111; font-style: normal; }
  .contact strong { font-weight: 700; }
</style>
</head>
<body>
  <div class="page-label page-label--front">Seite 1 | Titelseite</div>
  <div class="page-label page-label--back">Seite 2 | Rückseite</div>

  <section class="panel panel--front">
    <div class="band band--top"></div>
    <div class="photo photo--main" role="img" aria-label="Foto: Techniker spleisst Glasfasern an einem Hausverteilkasten"></div>
    <div class="photo photo--sat" role="img" aria-label="Foto: Satellitenschüsseln auf einem Dach"></div>
    <div class="photo photo--connectors" role="img" aria-label="Foto: Koaxial-Verteiler mit Kabeln"></div>
    <div class="photo photo--cables" role="img" aria-label="Foto: Cinch-Stecker in Gelb, Weiss und Rot"></div>
    <p class="services-line">GLASFASER | SATELLIT | KABEL | MULTIMEDIA</p>
    <div class="badge badge--partner">IHR<br>PARTNER!</div>
    <div class="brand brand--front">
      <span class="brand-square"></span>
      <span class="brand-name">KELLERHOF</span>
    </div>
    <div class="web web--front">www.kellerhof-av.ch</div>
    <div class="band band--bottom"></div>
  </section>

  <section class="panel panel--back">
    <div class="band band--top"></div>
    <h1 class="headline">Keinen Platz und schlechtes WLAN?<br>Die schnelle Glasfaser-Erweiterung:</h1>
    <div class="diagram" role="img" aria-label="Technische Zeichnung: Glasfaser-Erweiterung vom Hausverteilkasten über die OTO-Dose bis zur Internet-Box im Wohnzimmer"></div>
    <div class="diagram-partner">NovaCabl &amp; HomeFib</div>
    <div class="badge badge--solution">WIR<br>HABEN DIE<br>LÖSUNG!</div>

    <div class="offer-band"></div>
    <p class="offer-text">Vom Hausverteilkasten, ab OTO Dose direkt zum Router, zentral im Wohnzimmer</p>
    <div class="price-box">
      <div class="price-label">Pauschal sFr.</div>
      <div class="price-value">490,–</div>
    </div>

    <p class="intro">Seit 1997 sind wir Ihr Ansprechpartner für Installationen in den Bereichen Glasfasertechnik, FTTH, Kabel- und Satellitenempfang. Mit uns haben Sie den richtigen Partner um ein Projekt professionell zu realisieren.</p>
    <ul class="services">
      <li>FTTH und LumaKet als Partner der Gemeindewerk Lindmatt und Telvora</li>
      <li>Glasfaserinstallationen für Gewerbe, Banken und Versicherungen</li>
      <li>Störungsbehebung und Erweiterungen von bestehenden Anlagen</li>
      <li>Spleissungen, OTDR messen und Protokollieren</li>
    </ul>

    <div class="brand brand--back">
      <span class="brand-square"></span>
      <span class="brand-name">KELLERHOF</span>
    </div>

    <address class="contact">
      <strong>Kellerhof Audio und Video Installationen</strong><br>
      Lindenweg 12 | CH-8610 Ustermatt<br>
      Telefon: 044 555 18 20 | info@kellerhof-av.ch
    </address>
    <div class="web web--back">www.kellerhof-av.ch</div>
    <div class="band band--bottom"></div>
  </section>
</body>
</html>
```